VelmoraTrade (Trading Platform)

We need a design of VelmoraTrade Trading Platform.

Please find attached a mock up of VelmoraTrade design this has to be redesigned based on plinor.co.uk style.

Industry/Entity Type

Digital

```html
<!DOCTYPE html>
<html lang="en">
<head>
<meta charset="utf-8">
<title>VelmoraTrade – Trading Platform</title>
<link rel="stylesheet" href="https://fonts.googleapis.com/css2?family=Arimo:wght@400&family=Open+Sans:wght@400;600&display=swap">
<style>
:root{
  --brand:#0a9bd4;
  --brand-dark:#0787b9;
  --ink:#333;
  --muted:#666;
  --dark:#464646;
  --row-a:#dbe9f7;
  --row-b:#bcd9f2;
  --bid-a:#c6e3c6;
  --bid-b:#deefdc;
  --bid-ink:#3f973f;
  --ask-a:#d1bdd1;
  --ask-b:#e3d6e3;
  --ask-ink:#8b6b8b;
  --white:#fff;
  --ui-font:"Open Sans",Arial,sans-serif;
  --data-font:"Arimo",Arial,sans-serif;
}
*{box-sizing:border-box;margin:0;padding:0}
html,body{width:1200px;height:975px;overflow:hidden;background:var(--white)}
body{font-family:var(--data-font);color:var(--ink);font-size:12px}
.stage{position:relative;width:1100px;height:894px;transform:scale(1.0909);transform-origin:0 0}
.abs{position:absolute}

/* header */
.site-header{left:0;top:0;width:1100px;height:126px;background:var(--white);box-shadow:0 2px 4px rgba(0,0,0,.12);font-family:var(--ui-font)}
.brand{left:73px;top:52px;font-size:20px;font-weight:400;letter-spacing:2px;color:var(--dark)}
.brand-divider{left:234px;top:30px;width:1px;height:67px;background:#888}
.brand-dot{left:252px;top:41px;width:16px;height:16px;border-radius:50%;background:var(--brand)}
.main-nav{left:255px;top:83px;display:flex;gap:24px;font-size:12.5px;color:var(--muted)}
.field{height:31px;border:1px solid #bbb;border-radius:3px;background:var(--white);padding:8px 10px;font-size:12px;color:#777}
.btn{height:31px;border-radius:3px;color:var(--white);font-size:13.5px;text-align:center;line-height:31px}
.btn-login{left:873px;top:47px;width:69px;background:var(--dark)}
.btn-signup{left:956px;top:47px;width:70px;background:var(--brand)}

/* side tables */
.panel{width:139px}
.panel-head{height:23px;background:var(--brand);color:var(--white);font-family:var(--ui-font);font-size:13px;line-height:23px;padding:0 10px;display:flex;justify-content:space-between}
.row{height:24px;line-height:24px;padding:0 11px;font-size:12px;color:#666;display:flex;white-space:nowrap}
.row:nth-child(odd){background:var(--row-a)}
.row:nth-child(even){background:var(--row-b)}
.row .c1{width:64px}
.down{color:#c0392b;font-size:10px}
.up{color:#5aa85a;font-size:10px}

.chat{left:73px;top:495px;width:139px;height:235px;background:var(--row-a)}
.chat-tabs{display:flex;height:28px;background:var(--dark);font-size:12px;color:var(--white);line-height:28px;white-space:nowrap}
.chat-tabs span{text-align:center}
.chat-tabs .on{background:var(--brand)}
.chat-log{padding:12px 11px;font-size:11px;line-height:19px}
.chat-log .user{color:var(--brand)}
.chat-log b{font-weight:400;font-size:13px;color:#333}
.chat-input{position:absolute;left:0;bottom:0;width:139px;height:23px;line-height:23px;background:#c5d9ec;font-size:11px;color:#555;padding:0 8px;white-space:nowrap;overflow:hidden}

/* chart toolbar */
.toolbar{left:233px;top:161px;width:540px;height:45px;background:var(--dark);font-family:var(--ui-font)}
.tool{position:absolute;top:12px;height:23px;background:var(--brand);color:var(--white);font-size:12px;line-height:23px;white-space:nowrap}
.tool .caret{position:absolute;right:0;top:0;width:23px;height:23px;border-left:1px solid #7cc9e8}
.tool .caret::after{content:"";position:absolute;left:6px;top:9px;border:5px solid transparent;border-top-color:var(--white)}
.subbar{left:233px;top:206px;width:540px;height:48px;background:linear-gradient(#fdfdfd,#dedede);border-bottom:1px solid #ccc;font-family:var(--ui-font)}
.ohlc{font-size:12px;color:#555;white-space:nowrap}

/* chart */
.chart{left:226px;top:264px}

/* orders */
.tabs{left:233px;top:606px;display:flex;height:24px;font-family:var(--ui-font);font-size:12px;line-height:24px}
.tabs span{background:#d4d4d4;color:#555;padding:0 7px}
.tabs .on{background:var(--brand);color:var(--white)}
.orders{left:233px;top:630px;width:540px;border-collapse:collapse;font-size:12px;table-layout:fixed}
.orders th{background:var(--brand-dark);color:var(--white);font-weight:400;text-align:left;height:29px;padding:0 10px}
.orders td{height:24px;padding:0 10px;color:#555}
.orders tbody tr:nth-child(odd) td{background:var(--row-a)}
.orders tbody tr:nth-child(even) td{background:var(--row-b)}
.orders th+th,.orders td+td{border-left:1px dotted #8aa}

/* trade box */
.mode{left:793px;top:163px;display:flex;font-family:var(--ui-font);font-size:13px;color:var(--white);line-height:29px;text-align:center}
.mode span{width:110px}
.mode .market{background:var(--brand)}
.mode .limit{background:var(--dark)}
.quote{top:192px;width:110px;height:51px;text-align:center;color:#444;font-size:14px;padding-top:8px;line-height:17px}
.quote big{font-size:17px}
.quote small{font-size:13px}
.sell{left:793px;background:#c3dcf2}
.buy{left:903px;background:#a7cdef}
.qty{top:243px;width:110px;height:23px;line-height:23px;text-align:center;color:var(--white);font-size:12px}
.qty-sell{left:793px;background:#9dc4e8}
.qty-buy{left:903px;background:#82b3e2}
.label{top:270px;font-size:12px;color:#444}
.input{top:288px;height:24px;border:1px solid #bbb;font-size:13px;color:#444;padding:0 7px;line-height:22px}

/* order book */
.book{left:793px;top:323px;width:220px}
.book-head{height:24px;background:var(--brand);color:var(--white);font-family:var(--ui-font);font-size:13px;line-height:24px;display:flex;padding-left:9px}
.book-head span:first-child,.book-row span:first-child{width:119px}
.book-row{height:24px;line-height:24px;font-size:12px;display:flex;padding-left:11px}
.bid{color:var(--bid-ink)}
.bid:nth-child(odd){background:var(--bid-a)}
.bid:nth-child(even){background:var(--bid-b)}
.ask{color:var(--ask-ink)}
.ask:nth-child(odd){background:var(--ask-a)}
.ask:nth-child(even){background:var(--ask-b)}

/* footer */
.site-footer{left:0;top:783px;width:1100px;height:111px;background:var(--brand);color:var(--white);font-size:12px}
.footer-links{position:absolute;left:72px;top:35px;white-space:nowrap}
.copyright{position:absolute;left:72px;top:65px;white-space:nowrap}
.social{position:absolute;top:43px;width:28px;height:28px;border-radius:50%;background:var(--white)}
</style>
</head>
<body>
<div class="stage">

  <header class="site-header abs">
    <div class="brand abs">VelmoraTrade</div>
    <div class="brand-divider abs"></div>
    <div class="brand-dot abs"></div>
    <nav class="main-nav abs"><span>Home</span><span>About</span><span>Trading</span><span>Support</span></nav>
    <div class="field abs" style="left:558px;top:47px;width:143px">Email</div>
    <div class="field abs" style="left:715px;top:47px;width:143px">Password</div>
    <div class="btn btn-login abs">Log In</div>
    <div class="btn btn-signup abs">Sign Up</div>
  </header>

  <section class="panel abs" style="left:73px;top:163px">
    <div class="panel-head"><span>PAIR</span><span>PRICE</span></div>
    <div>
      <div class="row"><span class="c1">BTC/USD</span><span><span class="down">⬇</span> 634.12</span></div>
      <div class="row"><span class="c1">LTC/USD</span><span><span class="down">⬇</span> 23.23</span></div>
      <div class="row"><span class="c1">LTC/BTC</span><span><span class="up">⬆</span> 0.0123</span></div>
      <div class="row"></div>
      <div class="row"></div>
    </div>
  </section>

  <section class="panel abs" style="left:73px;top:329px">
    <div class="panel-head"><span>YOUR BALANCE</span></div>
    <div>
      <div class="row"><span class="c1">BTC</span><span>0.92176</span></div>
      <div class="row"><span class="c1">LTC</span><span>0</span></div>
      <div class="row"><span class="c1">USD</span><span>1987.45</span></div>
      <div class="row"></div>
      <div class="row"></div>
    </div>
  </section>

  <section class="chat abs">
    <div class="chat-tabs"><span class="on" style="width:41px">Chat</span><span style="width:46px">News</span><span style="width:52px">Chirper</span></div>
    <div class="chat-log">
      <div><span class="user">User1:</span> <b>Hello!</b></div>
      <div>User2: Hi!</div>
    </div>
    <div class="chat-input">Type your message here</div>
  </section>

  <div class="toolbar abs">
    <div class="abs" style="left:10px;top:12px;width:65px;height:23px;background:var(--white)"></div>
    <div class="tool" style="left:75px;width:49px;padding-left:6px">ID<span class="caret"></span></div>
    <div class="tool" style="left:148px;width:106px;padding-left:20px">CHART<span class="caret"></span></div>
    <div class="tool" style="left:280px;width:106px;padding-left:18px">STUDIES<span class="caret"></span></div>
    <div class="tool" style="left:411px;width:62px">
      <svg width="14" height="14" viewBox="0 0 14 14" style="position:absolute;left:12px;top:5px"><circle cx="7" cy="7" r="5" fill="none" stroke="#fff" stroke-width="2" stroke-dasharray="2 1.2"/><circle cx="7" cy="7" r="2" fill="none" stroke="#fff" stroke-width="1.2"/></svg>
      <span class="caret"></span></div>
    <div class="tool" style="left:495px;width:34px;text-align:center">F</div>
  </div>
  <div class="subbar abs">
    <div class="tool" style="left:10px;top:14px;width:106px;padding-left:11px">Select Tool<span class="caret"></span></div>
    <div class="ohlc abs" style="left:316px;top:7px">O: 141.98</div>
    <div class="ohlc abs" style="left:385px;top:7px">H: 141.98</div>
    <div class="ohlc abs" style="left:455px;top:7px">V: 141.98</div>
    <div class="ohlc abs" style="left:316px;top:29px">C: 141.09</div>
    <div class="ohlc abs" style="left:385px;top:29px">L: 141.09</div>
  </div>

  <svg class="chart abs" width="550" height="310" viewBox="226 264 550 310" font-family="Arimo, Arial, sans-serif" font-size="10" fill="#666">
    <g stroke="#c8c8c8" stroke-width="1">
      <line x1="238" y1="270" x2="773" y2="270"/><line x1="238" y1="326" x2="773" y2="326"/>
      <line x1="238" y1="382" x2="773" y2="382"/><line x1="238" y1="438" x2="773" y2="438"/>
      <line x1="238" y1="493" x2="773" y2="493"/><line x1="238" y1="549" x2="773" y2="549"/>
      <line x1="238" y1="270" x2="238" y2="549"/><line x1="306" y1="270" x2="306" y2="549"/>
      <line x1="375" y1="270" x2="375" y2="549"/><line x1="443" y1="270" x2="443" y2="549"/>
      <line x1="512" y1="270" x2="512" y2="549"/><line x1="580" y1="270" x2="580" y2="549"/>
      <line x1="649" y1="270" x2="649" y2="549"/><line x1="717" y1="270" x2="717" y2="549"/>
    </g>
    <path fill="#a9cdec" fill-opacity=".8" stroke="#5bb6e0" stroke-width="1"
      d="M238 401 L252 396 272 397 292 398 306 385 320 394 334 384 348 382 361 376 375 389 389 394 402 402 416 394 430 402 443 389 457 396 470 398 484 397 497 382 512 388 525 401 538 400 552 391 566 387 580 380 594 376 608 364 622 353 635 347 649 352 663 366 677 376 690 385 704 383 717 383 731 391 745 387 760 382 773 380 L773 549 238 549Z"/>
    <g text-anchor="start">
      <text x="232" y="279">100</text><text x="232" y="335">80</text><text x="232" y="391">60</text>
      <text x="232" y="447">40</text><text x="232" y="502">20</text><text x="232" y="559">0</text>
    </g>
    <g text-anchor="middle">
      <text x="241" y="564">0</text><text x="306" y="564">5</text><text x="375" y="564">10</text>
      <text x="443" y="564">15</text><text x="517" y="564">20</text><text x="580" y="564">25</text>
      <text x="649" y="564">30</text><text x="717" y="564">35</text>
    </g>
  </svg>

  <div class="tabs abs"><span class="on">Orders</span><span>History</span><span>Transactions</span></div>
  <table class="orders abs">
    <colgroup><col style="width:122px"><col style="width:260px"><col style="width:80px"><col></colgroup>
    <thead><tr><th>Ticker</th><th>Time <span style="float:right;font-size:8px">▲</span></th><th>Price <span style="float:right;font-size:8px">⇕</span></th><th>Volume</th></tr></thead>
    <tbody>
      <tr><td>BTC/USD</td><td>12:23 12.10.2014</td><td>634.34</td><td>0.23</td></tr>
      <tr><td>LTC/USD</td><td>11:23 12.10.2014</td><td>23.45</td><td>0.01</td></tr>
      <tr><td></td><td></td><td></td><td></td></tr>
    </tbody>
  </table>

  <div class="mode abs"><span class="market">MARKET</span><span class="limit">LIMIT</span></div>
  <div class="quote sell abs">Limit SELL<br><small>157</small><big>5.60</big></div>
  <div class="quote buy abs">Limit BUY<br><small>157</small><big>5.71</big></div>
  <svg class="abs" style="left:886px;top:196px" width="8" height="40" viewBox="0 0 8 40"><line x1="4" y1="2" x2="4" y2="38" stroke="#fff"/><path d="M1 6 L4 1 7 6" fill="none" stroke="#fff"/></svg>
  <div class="qty qty-sell abs">Qty&nbsp;&nbsp;20.0</div>
  <div class="qty qty-buy abs">Qty&nbsp;&nbsp;20.0</div>
  <div class="label abs" style="left:793px">Quantity</div>
  <div class="label abs" style="left:865px">Limit</div>
  <div class="input abs" style="left:793px;width:68px">50</div>
  <div class="input abs" style="left:865px;width:148px">1576.63</div>

  <section class="book abs">
    <div class="book-head"><span>PRICE</span><span>VOLUME</span></div>
    <div>
      <div class="book-row bid"><span>123</span><span>0.233</span></div>
      <div class="book-row bid"><span>122</span><span>0.334</span></div>
      <div class="book-row bid"><span>119</span><span>2.321</span></div>
      <div class="book-row bid"><span>118</span><span>0.343</span></div>
      <div class="book-row bid"><span>117</span><span>0.22</span></div>
      <div class="book-row bid"><span>116</span><span>0.025</span></div>
      <div class="book-row bid"><span>115</span><span>0.5246</span></div>
      <div class="book-row bid"><span>114</span><span>0.546</span></div>
      <div class="book-row ask"><span>113</span><span>1.275</span></div>
      <div class="book-row ask"><span>112</span><span>2.343</span></div>
      <div class="book-row ask"><span>111</span><span>0.232</span></div>
      <div class="book-row ask"><span>110</span><span>0.244</span></div>
      <div class="book-row ask"><span>109</span><span>0.821</span></div>
      <div class="book-row ask"><span>108</span><span>0.523</span></div>
      <div class="book-row ask"><span>109</span><span>0.821</span></div>
      <div class="book-row ask"><span>108</span><span>0.523</span></div>
    </div>
  </section>

  <footer class="site-footer abs">
    <div class="footer-links">Terms and Conditions | Privacy Policy | FAQ's | Contact Us</div>
    <div class="copyright">Copyright © 2013. All Rights Reserved.</div>
    <span class="social" style="left:907px"></span>
    <span class="social" style="left:947px"></span>
    <span class="social" style="left:988px"></span>
  </footer>

</div>
</body>
</html>
```